Steady Harvest of Patrons Programme Graphic

Please refer to attached graphic.
I wish to redesign this graphic to represent a programme of work that we (Brinvo) deliver to our customers.
The design represents 9 steps ( 3 steps at each of 3 levels) and is all about implementing the 'Steady Harvest of Patrons'

I like the fact that the increasing business growth is evident when you are progressing through the stages, but the current graphic looks dated and the colours are not working.
I would also like to incorporate the SHP logo we have created.

Target Market(s)

IT Sector - businesses looking to grow

Industry/Entity Type

We are a digital marketing company

Requirements
Must have
• Clear, concise design
Should not have
• Design must not be complicated

```html
<!DOCTYPE html>
<html lang="en">
<head>
<meta charset="utf-8">
<title>Steady Harvest of Patrons – Programme</title>
<link rel="stylesheet" href="https://fonts.googleapis.com/css2?family=Outfit:wght@400;500;600&display=swap">
<style>
  :root {
    --backdrop: #7a7a7a;
    --paper: #ffffff;
    --ink-navy: #1f1a4e;
    --card-top: #231c50;
    --card-bottom: #1b5c95;
    --footer: #1a69a7;
    --accent: #5ad6f5;
    --arrow-top: #5ad6f5;
    --arrow-mid: #1596d6;
    --white: #ffffff;
  }
  html, body {
    margin: 0;
    padding: 0;
    width: 1200px;
    height: 702px;
    overflow: hidden;
    background: var(--backdrop);
  }
  .programme-graphic {
    display: block;
    width: 1200px;
    height: 702px;
    font-family: "Outfit", sans-serif;
  }
  .axis-label { font-size: 22px; font-weight: 600; fill: var(--ink-navy); }
  .brand-name { font-size: 46px; font-weight: 600; fill: var(--arrow-mid); letter-spacing: 1px; }
  .programme-title { font-size: 24px; font-weight: 600; fill: var(--ink-navy); }
  .badge-name { font-size: 15px; font-weight: 600; fill: var(--arrow-mid); }
  .step-number { font-size: 30px; font-weight: 500; fill: var(--white); }
  .step-heading { font-size: 22px; font-weight: 500; fill: var(--accent); }
  .step-item { font-size: 16px; font-weight: 400; fill: var(--white); }
  .bullet { fill: none; stroke: var(--accent); stroke-width: 1.3; }
  .footer-title { font-size: 14.5px; font-weight: 400; fill: var(--accent); }
  .footer-sub { font-size: 9.5px; font-weight: 500; fill: var(--white); letter-spacing: 3.6px; }
  .icon-line { fill: none; stroke: #1a82c4; stroke-width: 3; stroke-linejoin: round; stroke-linecap: round; }
</style>
</head>
<body>
<svg class="programme-graphic" viewBox="0 0 1200 702" xmlns="http://www.w3.org/2000/svg">
  <defs>
    <linearGradient id="arrowShaft" x1="0" y1="0" x2="0" y2="1">
      <stop offset="0" stop-color="var(--arrow-mid)"/>
      <stop offset="0.55" stop-color="var(--arrow-mid)"/>
      <stop offset="1" stop-color="#ffffff"/>
    </linearGradient>
    <linearGradient id="cardFill" x1="0" y1="0" x2="0" y2="1">
      <stop offset="0" stop-color="var(--card-top)"/>
      <stop offset="1" stop-color="var(--card-bottom)"/>
    </linearGradient>
    <linearGradient id="circleFill" x1="0" y1="1" x2="1" y2="0">
      <stop offset="0" stop-color="#1a8fd0"/>
      <stop offset="1" stop-color="#2a2a5e"/>
    </linearGradient>
    <radialGradient id="meshTone" cx="0.5" cy="0.5" r="0.6">
      <stop offset="0" stop-color="#bfeefa" stop-opacity="0.55"/>
      <stop offset="1" stop-color="#ffffff" stop-opacity="0"/>
    </radialGradient>
    <clipPath id="clipStep1"><path d="M207,398 Q207,389 216,386 L470,323 Q479,321 479,330 L479,524 L207,524 Z"/></clipPath>
    <clipPath id="clipStep2"><path d="M503,326 Q503,317 512,314 L767,251 Q776,249 776,258 L776,524 L503,524 Z"/></clipPath>
    <clipPath id="clipStep3"><path d="M800,255 Q800,246 809,243 L1063,180 Q1072,178 1072,187 L1072,524 L800,524 Z"/></clipPath>
  </defs>

  <!-- Canvas -->
  <rect class="design-paper" x="71" y="76" width="1059" height="551" fill="var(--paper)"/>
  <rect class="background-mesh" role="img" aria-label="Soft wave-shaped wireframe mesh pattern in light cyan behind the steps" x="71" y="220" width="1059" height="400" fill="url(#meshTone)"/>

  <!-- Growth axis -->
  <g class="value-axis">
    <rect x="158" y="150" width="16" height="450" fill="url(#arrowShaft)"/>
    <polygon points="166,123 203,160 191,173 166,148 141,173 129,160" fill="var(--arrow-top)"/>
    <text class="axis-label" transform="translate(139,458) rotate(-90)">Business Value</text>
  </g>

  <!-- Brand -->
  <g class="brand">
    <rect x="232" y="131" width="28" height="28" fill="var(--arrow-mid)"/>
    <text class="brand-name" x="270" y="166">Brinvo</text>
  </g>

  <!-- Programme title -->
  <g class="programme-header">
    <text class="programme-title" x="651" y="141">Steady Harvest of Patrons</text>
    <rect x="1040" y="110" width="48" height="48" fill="none" stroke="var(--arrow-mid)" stroke-width="3"/>
    <text class="badge-name" x="1064" y="139" text-anchor="middle">SHP</text>
  </g>

  <!-- Step 01 -->
  <g class="step step-rhythmic">
    <path d="M207,398 Q207,389 216,386 L470,323 Q479,321 479,330 L479,524 L207,524 Z" fill="url(#cardFill)"/>
    <circle cx="479" cy="336" r="66" fill="url(#circleFill)" clip-path="url(#clipStep1)"/>
    <text class="step-number" x="446" y="378" text-anchor="middle">01</text>
    <text class="step-heading" x="232" y="418">Rhythmic</text>
    <circle class="bullet" cx="234" cy="442" r="3"/><text class="step-item" x="247" y="448">Personas</text>
    <circle class="bullet" cx="234" cy="470" r="3"/><text class="step-item" x="247" y="477">Database</text>
    <circle class="bullet" cx="234" cy="497" r="3"/><text class="step-item" x="247" y="504">Systems</text>
    <rect class="step-icon" role="img" aria-label="Connected systems icon" x="382" y="444" width="74" height="60" rx="6" fill="#1d6fae" opacity="0.45"/>
    <rect x="207" y="530" width="272" height="63" rx="8" fill="var(--footer)"/>
    <text class="footer-title" x="343" y="558" text-anchor="middle">Numbers that Matter</text>
    <text class="footer-sub" x="343" y="575" text-anchor="middle">FOUNDATION METRICS</text>
  </g>

  <!-- Step 02 -->
  <g class="step step-acquisition">
    <path d="M503,326 Q503,317 512,314 L767,251 Q776,249 776,258 L776,524 L503,524 Z" fill="url(#cardFill)"/>
    <circle cx="776" cy="264" r="66" fill="url(#circleFill)" clip-path="url(#clipStep2)"/>
    <text class="step-number" x="743" y="306" text-anchor="middle">02</text>
    <text class="step-heading" x="528" y="382">Acquisition</text>
    <circle class="bullet" cx="531" cy="409" r="3"/><text class="step-item" x="544" y="415">Messaging</text>
    <circle class="bullet" cx="531" cy="437" r="3"/><text class="step-item" x="544" y="444">Leads</text>
    <circle class="bullet" cx="531" cy="464" r="3"/><text class="step-item" x="544" y="470">Pipeline</text>
    <rect class="step-icon" role="img" aria-label="Lead attraction icon" x="692" y="436" width="68" height="68" rx="6" fill="#1d6fae" opacity="0.45"/>
    <rect x="503" y="530" width="273" height="63" rx="8" fill="var(--footer)"/>
    <text class="footer-title" x="640" y="558" text-anchor="middle">Weekly Scorecard</text>
    <text class="footer-sub" x="640" y="575" text-anchor="middle">TACTICAL EXECUTION</text>
  </g>

  <!-- Step 03 -->
  <g class="step step-customers">
    <path d="M800,255 Q800,246 809,243 L1063,180 Q1072,178 1072,187 L1072,524 L800,524 Z" fill="url(#cardFill)"/>
    <circle cx="1072" cy="193" r="66" fill="url(#circleFill)" clip-path="url(#clipStep3)"/>
    <text class="step-number" x="1039" y="235" text-anchor="middle">03</text>
    <text class="step-heading" x="824" y="344">Customers</text>
    <circle class="bullet" cx="827" cy="370" r="3"/><text class="step-item" x="840" y="377">Sales</text>
    <circle class="bullet" cx="827" cy="398" r="3"/><text class="step-item" x="840" y="405">Nurture</text>
    <circle class="bullet" cx="827" cy="425" r="3"/><text class="step-item" x="840" y="431">Reference</text>
    <g class="step-icon growth-chart">
      <rect class="icon-line" x="989" y="472" width="11" height="28"/>
      <rect class="icon-line" x="1008" y="462" width="11" height="38"/>
      <rect class="icon-line" x="1027" y="450" width="11" height="50"/>
      <line class="icon-line" x1="983" y1="502" x2="1050" y2="502"/>
      <polyline class="icon-line" points="986,463 1005,446 1014,452 1030,438 1040,444 1044,430"/>
      <polyline class="icon-line" points="1036,429 1044,429 1044,437"/>
    </g>
    <rect x="800" y="530" width="272" height="63" rx="8" fill="var(--footer)"/>
    <text class="footer-title" x="936" y="558" text-anchor="middle">Monthly Scorecard</text>
    <text class="footer-sub" x="936" y="575" text-anchor="middle">STRATEGIC REVIEW</text>
  </g>
</svg>
</body>
</html>
```